Navelo Partnering Business Card

Hello everyone. We need a business card design that would match our logo and the theme we're trying to have for Navelo that you can find on our website and/or Corvapage page

```html
<!DOCTYPE html>
<html lang="en">
<head>
<meta charset="utf-8">
<title>Navelo Partnering Business Card</title>
<link rel="stylesheet" href="https://fonts.googleapis.com/css2?family=Montserrat:wght@600;700&family=Roboto:wght@300;400&display=swap">
<style>
  :root {
    --backdrop: #333334;
    --card: #262627;
    --edge: #4a3c8c;
    --ink: #ffffff;
    --ink-soft: #e6e6e6;
    --rule: #8a8a8a;
  }
  * { box-sizing: border-box; margin: 0; padding: 0; }
  html, body { width: 1200px; height: 900px; overflow: hidden; }
  body {
    background: var(--backdrop);
    display: flex;
    flex-direction: column;
    align-items: center;
    justify-content: center;
    gap: 36px;
    font-family: "Roboto", Arial, sans-serif;
    color: var(--ink);
  }
  .card {
    position: relative;
    width: 740px;
    height: 400px;
    background: var(--card);
    border-bottom: 7px solid var(--edge);
  }
  .brand-name {
    font-family: "Montserrat", Arial, sans-serif;
    font-weight: 700;
    color: var(--ink);
    letter-spacing: 1px;
    line-height: 1;
  }
  .card-front {
    display: flex;
    align-items: center;
    justify-content: center;
  }
  .card-front .brand-name { font-size: 72px; }
  .card-back { display: flex; align-items: center; }
  .back-brand {
    width: 330px;
    display: flex;
    justify-content: center;
  }
  .back-brand .brand-name { font-size: 58px; }
  .divider {
    width: 1px;
    height: 250px;
    background: var(--rule);
  }
  .contact { padding-left: 40px; }
  .person-name {
    font-family: "Montserrat", Arial, sans-serif;
    font-weight: 700;
    font-size: 26px;
    letter-spacing: 1px;
  }
  .person-role {
    font-size: 18px;
    font-weight: 300;
    color: var(--ink-soft);
    margin-top: 2px;
  }
  .address {
    font-size: 18px;
    font-weight: 300;
    color: var(--ink-soft);
    margin-top: 18px;
    line-height: 1.35;
  }
  .contact-list { list-style: none; margin-top: 16px; }
  .contact-list li {
    display: flex;
    align-items: center;
    gap: 14px;
    font-size: 18px;
    font-weight: 300;
    color: var(--ink-soft);
    line-height: 1.3;
  }
  .contact-list svg { width: 16px; height: 16px; flex: none; }
</style>
</head>
<body>
  <section class="card card-front">
    <span class="brand-name">Navelo</span>
  </section>

  <section class="card card-back">
    <div class="back-brand">
      <span class="brand-name">Navelo</span>
    </div>
    <div class="divider"></div>
    <div class="contact">
      <p class="person-name">Daniel REYES</p>
      <p class="person-role">Managing Director</p>
      <p class="address">28-10 96th Avenue<br>Riverside Point, NY 11402-2210</p>
      <ul class="contact-list">
        <li>
          <svg viewBox="0 0 16 16" fill="none" stroke="#fff" stroke-width="1.3"><path d="M4 1.5l2.5 3-1.5 1.5c.8 1.8 2.2 3.2 4 4l1.5-1.5 3 2.5-1.5 2c-5 0-10-5-10-10z"/></svg>
          000.000.0000
        </li>
        <li>
          <svg viewBox="0 0 16 16" fill="none" stroke="#fff" stroke-width="1.3"><rect x="4.5" y="1" width="7" height="14" rx="1.2"/><line x1="7" y1="12.5" x2="9" y2="12.5"/></svg>
          000.000.0000
        </li>
        <li>
          <svg viewBox="0 0 16 16" fill="none" stroke="#fff" stroke-width="1.3"><rect x="1" y="3" width="14" height="10"/><path d="M1 3l7 6 7-6"/></svg>
          daniel@navelopartnering.com
        </li>
        <li>
          <svg viewBox="0 0 16 16" fill="none" stroke="#fff" stroke-width="1.2"><circle cx="8" cy="8" r="6.5"/><ellipse cx="8" cy="8" rx="3" ry="6.5"/><line x1="1.5" y1="8" x2="14.5" y2="8"/></svg>
          www.navelopartnering.com
        </li>
      </ul>
    </div>
  </section>
</body>
</html>
```